Heron Dusk business card design

I make handmade colourful women's beaded jewellery (necklaces and earnings).
I require a business card to be designed to truly reflect my jewellery, that is, it is different and stands out.
I would like the business card to look creative, arty, gentle and feminine and fit in with the look of my website and logo (already developed).
I would like the business card to have strong use of the water reeds that are flowing in the wind (please see the banner image on my website www.herondusk-example.com and attached files).

Target Market(s)

Women who are fashion conscious, hip and funky. My audience like things that are a little different and stand out in a crowd.These women are aged in their 20's-40's.

Industry/Entity Type

Jewelry

Contact Information for Business Card

Please include the following items:
1) my logo: Heron Dusk
2) my name, address and phone number: Marla Dorsten, Sydney, Australia, 0400 000 000
3) my web details: www.herondusk-example.com, info@herondusk-example.com, www.facebook.com/herondusk

Font styles to use
Other font styles liked:
• Remachine Script

Requirements
Must have
• My business card must have the following:
• 1) my personal details including all my website contacts (see above).
• 2) Heron Dusk logo
• 3) Reeds flowing in the wind (see my banner image on my website www.herondusk-example.com or see attached files).
Nice to have
• A sunrise in the background (rising over water)
• I would prefer that the colour scheme to fit with the Heron Dusk logo, that is the colours of an early morning sunrise i.e yellows, oranges. The use of black and white is fine.
Should not have
• I do not like a commercial manufactured look with hard edges. I would like a look that is soft and reflects an artistic, creative and independent business.

```html
<!DOCTYPE html>
<html lang="en">
<head>
<meta charset="utf-8">
<title>Heron Dusk – Business Card</title>
<link rel="stylesheet" href="https://fonts.googleapis.com/css2?family=Kaushan+Script&family=PT+Serif:wght@400;700&display=swap">
<style>
  :root {
    --backdrop: #e9e8e6;
    --card-white: #ffffff;
    --card-dark: #2a2a2a;
    --sun-orange: #f29a12;
    --sun-yellow: #fbc531;
    --ink: #1d1d1d;
    --light-text: #f4f4f4;
  }
  html, body {
    margin: 0;
    width: 1200px;
    height: 1000px;
    overflow: hidden;
    background: var(--backdrop);
  }
  .card {
    position: absolute;
    left: 75px;
    top: 200px;
    width: 1050px;
    height: 600px;
    background: var(--card-white);
    border-radius: 6px;
    overflow: hidden;
    box-shadow: 0 10px 30px rgba(0,0,0,0.18);
  }
  .card__waves {
    position: absolute;
    inset: 0;
    width: 100%;
    height: 100%;
  }
  .brand {
    position: absolute;
    left: 70px;
    top: 60px;
    display: flex;
    align-items: center;
    gap: 22px;
  }
  .brand__disc {
    width: 120px;
    height: 120px;
    border-radius: 50%;
    background: radial-gradient(circle at 50% 40%, var(--sun-yellow), var(--sun-orange));
    border: 4px solid var(--ink);
  }
  .brand__name {
    font-family: "PT Serif", Georgia, serif;
    font-size: 42px;
    font-weight: 400;
    color: var(--ink);
  }
  .holder {
    position: absolute;
    right: 60px;
    top: 110px;
    text-align: right;
  }
  .holder__name {
    font-family: "Kaushan Script", cursive;
    font-size: 54px;
    color: var(--ink);
    line-height: 1;
  }
  .holder__role {
    font-family: "Kaushan Script", cursive;
    font-size: 30px;
    color: var(--sun-orange);
    margin-top: 8px;
  }
  .contacts {
    position: absolute;
    right: 55px;
    top: 378px;
    margin: 0;
    padding: 0;
    list-style: none;
    font-family: "PT Serif", Georgia, serif;
    font-size: 29px;
    color: var(--light-text);
  }
  .contacts__item {
    display: flex;
    justify-content: flex-end;
    align-items: center;
    gap: 22px;
    height: 47px;
  }
  .contacts__icon {
    width: 26px;
    height: 26px;
    flex: none;
    fill: var(--light-text);
  }
</style>
</head>
<body>
  <article class="card">
    <svg class="card__waves" viewBox="0 0 1050 600" preserveAspectRatio="none" aria-hidden="true">
      <path d="M0 250 C 250 330, 450 360, 650 310 C 820 268, 950 240, 1050 236 L1050 262 C 950 266, 820 292, 650 334 C 450 384, 250 350, 0 286 Z" fill="var(--sun-orange)"/>
      <path d="M0 300 C 250 366, 450 398, 650 350 C 820 310, 950 282, 1050 276" fill="none" stroke="var(--card-dark)" stroke-width="6"/>
      <path d="M0 318 C 250 384, 450 414, 650 368 C 820 330, 950 302, 1050 296 L1050 600 L0 600 Z" fill="var(--card-dark)"/>
      <path d="M0 342 C 250 404, 450 430, 650 386 C 820 348, 950 322, 1050 316" fill="none" stroke="var(--card-white)" stroke-width="3"/>
    </svg>

    <div class="brand">
      <div class="brand__disc"></div>
      <span class="brand__name">Heron Dusk</span>
    </div>

    <div class="holder">
      <div class="holder__name">Jonah Stell</div>
      <div class="holder__role">CEO/Founder</div>
    </div>

    <ul class="contacts">
      <li class="contacts__item">0400 000 000
        <svg class="contacts__icon" viewBox="0 0 24 24"><path d="M6.6 10.8a15 15 0 0 0 6.6 6.6l2.2-2.2a1 1 0 0 1 1-.25 11.4 11.4 0 0 0 3.6.57 1 1 0 0 1 1 1V20a1 1 0 0 1-1 1A17 17 0 0 1 3 4a1 1 0 0 1 1-1h3.5a1 1 0 0 1 1 1c0 1.25.2 2.45.57 3.57a1 1 0 0 1-.25 1z"/></svg>
      </li>
      <li class="contacts__item">info@herondusk-example.com
        <svg class="contacts__icon" viewBox="0 0 24 24"><path d="M2 5h20v14H2z M4 7v.5l8 5 8-5V7z" fill-rule="evenodd"/></svg>
      </li>
      <li class="contacts__item">www.herondusk-example.com
        <svg class="contacts__icon" viewBox="0 0 24 24"><circle cx="12" cy="12" r="10"/><path d="M2 12h20M12 2c3 3 3 17 0 20M12 2c-3 3-3 17 0 20" stroke="var(--card-dark)" stroke-width="1.6" fill="none"/></svg>
      </li>
      <li class="contacts__item">Marla Dorsten, Sydney, Australia
        <svg class="contacts__icon" viewBox="0 0 24 24"><path d="M12 2a7 7 0 0 0-7 7c0 5 7 13 7 13s7-8 7-13a7 7 0 0 0-7-7zm0 9.5A2.5 2.5 0 1 1 12 6.5a2.5 2.5 0 0 1 0 5z"/></svg>
      </li>
    </ul>
  </article>
</body>
</html>
```